Tranquil Pathway Business Card

Logo attached. (will be printing onto thick white/off white textured card)

Double sided business card for two Therapists working at Tranquil Pathway.

Require one design, but with different name and mobile numbers on each card.

Target Market(s)

Medical, Health

Industry/Entity Type

Business

Contact Information for Business Card

Need one business card design, but a separate card for each person - Colin Marchetti and Marieke de Boeckx.

FRONT OF CARD

Logo

Name (Colin Marchetti on one card, Marieke de Boeckx on the other)
Professional Clinical Hypnotherapist

Consulting Rooms (Near Lindqvist Hospital)
482 Brackenfield Road
Dunmore VIC 3987

Colin@TranquilPathway.example.au OR Marieke@TranquilPathway.example.au

Mobile: 0455 872 604 (for Colin) OR
Mobile: 0467 290 518 (for Marieke)

BACK OF CARD

Logo

Website: www.TranquilPathway.example.au

Phone: 1300 958 471

Requirements
Must have
• Text and logo only. No additiional graphics.

```html
<!DOCTYPE html>
<html lang="en">
<head>
<meta charset="utf-8">
<title>Tranquil Pathway Business Card</title>
<link rel="stylesheet" href="https://fonts.googleapis.com/css2?family=Montserrat:wght@700&family=Open+Sans:wght@400;600&display=swap">
<style>
  :root {
    --navy: #1f2a63;
    --white: #ffffff;
    --grey: #6d6e71;
    --light-grey: #b9babc;
    --backdrop: #2b2b2d;
  }
  * { box-sizing: border-box; margin: 0; padding: 0; }
  html, body { width: 1200px; height: 900px; overflow: hidden; }
  body {
    background: var(--backdrop);
    position: relative;
    font-family: "Open Sans", Arial, sans-serif;
  }
  .card {
    position: absolute;
    left: 300px;
    width: 600px;
    height: 343px;
    border-radius: 22px;
    overflow: hidden;
  }
  .card--back { top: 70px; background: var(--navy); }
  .card--front { top: 467px; background: var(--white); }

  /* back */
  .back-brand {
    position: absolute; left: 120px; top: 92px;
    display: flex; align-items: center; gap: 22px;
  }
  .brand-circle {
    width: 110px; height: 110px; border-radius: 50%;
    border: 9px solid var(--white);
  }
  .brand-divider { width: 2px; height: 120px; background: var(--white); }
  .brand-name {
    font-family: "Montserrat", Arial, sans-serif;
    font-weight: 700; font-size: 34px; line-height: 1.05;
    letter-spacing: 1px; text-transform: uppercase;
    color: var(--white);
  }
  .back-contact {
    position: absolute; left: 30px; bottom: 26px;
    color: var(--white); font-size: 14px; line-height: 1.45;
  }
  .back-contact .row { display: flex; align-items: center; gap: 6px; }

  /* front */
  .front-band {
    position: absolute; left: 0; right: 0; top: 172px; bottom: 0;
    background: var(--navy);
    border-top: 6px solid var(--light-grey);
    box-shadow: 0 -10px 0 -4px var(--white);
  }
  .front-brand {
    position: absolute; left: 0; right: 0; top: 40px;
    text-align: center;
    font-family: "Montserrat", Arial, sans-serif;
    font-weight: 700; font-size: 28px; letter-spacing: 1px;
    text-transform: uppercase; color: var(--navy);
  }
  .front-circle {
    position: absolute; left: 240px; top: 100px;
    width: 120px; height: 120px; border-radius: 50%;
    background: var(--navy);
    border: 8px solid var(--grey);
    box-shadow: 0 0 0 4px var(--white);
  }
  .person {
    position: absolute; left: 20px; bottom: 18px; width: 268px;
    text-align: right; color: var(--white);
  }
  .person-name {
    font-family: "Montserrat", Arial, sans-serif;
    font-weight: 700; font-size: 21px; line-height: 1.25; text-transform: uppercase;
  }
  .person-role { font-size: 12px; font-weight: 600; line-height: 1.4; margin-bottom: 3px; }
  .person-address { font-size: 11.5px; line-height: 1.4; }
  .front-contact {
    position: absolute; left: 306px; bottom: 40px;
    color: var(--white); font-size: 13px; line-height: 1.55;
  }
  .front-contact .row { display: flex; align-items: center; gap: 7px; }
  .icon { width: 12px; height: 12px; flex: none; }
</style>
</head>
<body>

<section class="card card--back">
  <div class="back-brand">
    <div class="brand-circle"></div>
    <div class="brand-divider"></div>
    <div class="brand-name">Tranquil<br>Pathway</div>
  </div>
  <div class="back-contact">
    <div class="row">
      <svg class="icon" viewBox="0 0 12 12"><path d="M2.5 1l2 2.2-1 1.3a7 7 0 0 0 4 4l1.3-1 2.2 2-1.2 1.5C5 11 1 7 1 2.2z" fill="#fff"/></svg>
      1300 958 471
    </div>
    <div class="row">www.TranquilPathway.example.au</div>
  </div>
</section>

<section class="card card--front">
  <div class="front-brand">Tranquil Pathway</div>
  <div class="front-band"></div>
  <div class="front-circle"></div>
  <div class="person">
    <div class="person-name">Colin Marchetti</div>
    <div class="person-role">Professional Clinical Hypnotherapist</div>
    <div class="person-address">Consulting Rooms (Near Lindqvist Hospital)<br>482 Brackenfield Road<br>Dunmore VIC 3987</div>
  </div>
  <div class="front-contact">
    <div class="row">
      <svg class="icon" viewBox="0 0 12 12"><rect x="3" y="0.5" width="6" height="11" rx="1" fill="none" stroke="#fff"/><circle cx="6" cy="9.5" r="0.7" fill="#fff"/></svg>
      0455 872 604
    </div>
    <div class="row">
      <svg class="icon" viewBox="0 0 12 12"><rect x="0.5" y="2.5" width="11" height="7" fill="none" stroke="#fff"/><path d="M0.5 2.5L6 7l5.5-4.5" fill="none" stroke="#fff"/></svg>
      Colin@TranquilPathway.example.au
    </div>
    <div class="row">
      <svg class="icon" viewBox="0 0 12 12"><circle cx="6" cy="6" r="5.5" fill="none" stroke="#fff"/><path d="M0.5 6h11M6 0.5c-3 3-3 8 0 11M6 0.5c3 3 3 8 0 11" fill="none" stroke="#fff" stroke-width="0.8"/></svg>
      www.TranquilPathway.example.au
    </div>
  </div>
</section>

</body>
</html>
```